Medical Equipment Provider Postcard

We are a full service Durable Medical Equipment provider, ORVAN Medical Equipment. We specialize in home medical equipment like oxygen, CPAP/BiPAP, hospital beds, etc. We are a locallly owned and operated business which is important to our small community her in Missouri. We want a high quality, bright, informative postcard that we can hand out to our referral sources (nurses and physicians). I'm attaching our current tri-fold design, we want something more professional and eye-catching.

Industry/Entity Type

Medical

Requirements
Must have
• Our logo
Nice to have
• Our colors are bright blue, black and white but would love to see some eye-catching design ideas!

```html
<!DOCTYPE html>
<html lang="en">
<head>
<meta charset="utf-8">
<title>ORVAN Medical Equipment Postcard</title>
<link href="https://fonts.googleapis.com/css2?family=Oswald:wght@500;600&family=Source+Sans+3:wght@300;400;600;700&display=swap" rel="stylesheet">
<style>
:root{
  --backdrop:#7a4d2b;
  --blue:#1f55ad;
  --blue-deep:#213f96;
  --blue-cell:#3a56a6;
  --black:#161616;
  --lime:#bcd63a;
  --lime-text:#cfe34a;
  --white:#ffffff;
  --ink:#222;
  --grey:#e5e7eb;
}
*{margin:0;padding:0;box-sizing:border-box}
html,body{width:863px;height:1200px;overflow:hidden}
body{background:var(--backdrop);position:relative;font-family:"Source Sans 3",sans-serif;color:var(--ink)}
.card{position:absolute;width:671px;overflow:hidden;box-shadow:4px 4px 6px rgba(0,0,0,.35)}
.front{left:91px;top:74px;height:521px;background:var(--white)}
.back{left:88px;top:618px;height:518px;background:var(--blue-deep)}
.abs{position:absolute}
.condensed{font-family:"Oswald",sans-serif;font-weight:600}

/* front */
.front-head{left:0;top:0;width:100%;height:112px;background:var(--blue)}
.front-head h1{position:absolute;left:30px;top:19px;color:var(--white);font-size:27.5px;line-height:34px;letter-spacing:.2px}
.showroom-band{left:0;top:112px;width:100%;height:56px;background:var(--black)}
.showroom-band h2{position:absolute;left:30px;top:4px;color:var(--lime-text);font-size:30px;letter-spacing:.2px}
.order-tab{left:29px;top:158px;width:268px;height:32px;z-index:2}
.order-tab span{position:absolute;left:0;right:0;top:1px;text-align:center;color:var(--white);font-size:20px}
.photo-care{left:389px;top:168px;width:282px;height:302px;background:linear-gradient(160deg,#f0e6da 0%,#d9c9b4 45%,#c7d3e3 100%);z-index:1}
.brand-box{left:469px;top:97px;width:164px;height:86px;background:var(--white);text-align:center;padding-top:8px;z-index:3}
.brand-name{font-family:"Oswald",sans-serif;font-weight:600;font-size:36px;line-height:44px;color:var(--blue);letter-spacing:1px}
.brand-sub{font-family:"Oswald",sans-serif;font-weight:600;font-size:14px;line-height:18px;color:var(--blue);margin-top:6px}
.services-title{left:30px;top:200px;color:var(--blue);font-size:20px;font-weight:600}
.services{left:30px;top:234px;list-style:none;font-size:15.5px;line-height:20.3px;color:#333}
.services.col2{left:198px}
.services li{position:relative;padding-left:19px}
.services svg{position:absolute;left:0;top:4px}
.delivery{left:30px;top:370px;color:var(--blue);font-size:19.5px;line-height:24px;font-weight:400}
.call-band{left:0;top:470px;width:100%;height:51px;z-index:2}
.insurance{left:0;top:431px;width:269px;height:90px;z-index:3}
.insurance p{position:absolute;left:30px;top:7px;font-size:19px;line-height:22px;color:#111;font-weight:400}
.call{left:270px;top:474px;color:var(--white);font-size:27px;letter-spacing:.3px;z-index:3}

/* back */
.back-head{left:0;top:0;width:100%;height:66px;background:var(--blue)}
.back-head h2{position:absolute;left:30px;top:20px;color:var(--white);font-size:27px}
.van-frame{left:474px;top:22px;width:162px;height:100px;background:var(--white);padding:5px}
.van-photo{width:100%;height:100%;background:linear-gradient(180deg,#b58a64 0%,#b58a64 45%,#eeeeee 46%,#dcdcdc 100%)}
.locations{left:30px;top:72px;color:var(--white);font-size:22px;font-weight:300}
.local{left:188px;top:74px;color:var(--lime-text);font-size:20px;font-weight:400}
.serve{left:30px;top:102px;color:var(--white);font-size:15px}
.loc-cell{top:134px;height:80px;background:var(--blue-cell);color:var(--white);font-size:14.4px;line-height:18.4px;text-align:center;padding-top:4px}
.loc-cell b{font-weight:700}
.gallery{left:0;top:215px;width:100%;height:181px;background:var(--grey)}
.product{top:13px;height:150px;border:1px solid #b9bcc2;background:linear-gradient(180deg,#ffffff,#e9ebef)}
.visit-band{left:0;top:396px;width:100%;height:34px;background:var(--lime)}
.visit-band h3{position:absolute;left:0;right:0;top:1px;text-align:center;color:var(--white);font-size:24px;letter-spacing:.2px;text-shadow:1px 1px 1px rgba(0,0,0,.45)}
.about{left:30px;top:438px;width:612px;color:var(--white);font-size:15.5px;line-height:19.4px;text-align:justify}
.about b{font-weight:700}
</style>
</head>
<body>

<section class="card front">
  <div class="abs front-head"><h1 class="condensed">We are your hometown full service Durable Medical<br>Equipment Provider. We offer a large, local showroom.</h1></div>
  <div class="abs showroom-band"><h2 class="condensed">COME SEE OUR LARGE SHOWROOM!</h2></div>
  <div class="abs order-tab">
    <svg width="268" height="32" viewBox="0 0 268 32" class="abs"><path d="M0 0 H268 L248 32 H22 Z" fill="#a7c93a"/></svg>
    <span class="condensed">WE CAN SPECIAL ORDER!</span>
  </div>
  <div class="abs photo-care" role="img" aria-label="Nurse smiling beside a senior woman in a wheelchair holding a cup"></div>
  <div class="abs brand-box">
    <div class="brand-name">ORVAN</div>
    <div class="brand-sub">medical equipment</div>
  </div>

  <h3 class="abs services-title">Available Services:</h3>
  <ul class="abs services">
    <li><svg width="13" height="13" viewBox="0 0 13 13"><rect x="0.7" y="0.7" width="11.6" height="11.6" fill="none" stroke="#1f55ad" stroke-width="1.4"/><path d="M2.5 6.5 L5.5 9.5 L11 2.5" fill="none" stroke="#1f55ad" stroke-width="1.8"/></svg>Oxygen</li>
    <li><svg width="13" height="13" viewBox="0 0 13 13"><rect x="0.7" y="0.7" width="11.6" height="11.6" fill="none" stroke="#1f55ad" stroke-width="1.4"/><path d="M2.5 6.5 L5.5 9.5 L11 2.5" fill="none" stroke="#1f55ad" stroke-width="1.8"/></svg>Nebulizers</li>
    <li><svg width="13" height="13" viewBox="0 0 13 13"><rect x="0.7" y="0.7" width="11.6" height="11.6" fill="none" stroke="#1f55ad" stroke-width="1.4"/><path d="M2.5 6.5 L5.5 9.5 L11 2.5" fill="none" stroke="#1f55ad" stroke-width="1.8"/></svg>Wheelchairs</li>
    <li><svg width="13" height="13" viewBox="0 0 13 13"><rect x="0.7" y="0.7" width="11.6" height="11.6" fill="none" stroke="#1f55ad" stroke-width="1.4"/><path d="M2.5 6.5 L5.5 9.5 L11 2.5" fill="none" stroke="#1f55ad" stroke-width="1.8"/></svg>Diabetic shoes</li>
    <li><svg width="13" height="13" viewBox="0 0 13 13"><rect x="0.7" y="0.7" width="11.6" height="11.6" fill="none" stroke="#1f55ad" stroke-width="1.4"/><path d="M2.5 6.5 L5.5 9.5 L11 2.5" fill="none" stroke="#1f55ad" stroke-width="1.8"/></svg>Commodes</li>
    <li><svg width="13" height="13" viewBox="0 0 13 13"><rect x="0.7" y="0.7" width="11.6" height="11.6" fill="none" stroke="#1f55ad" stroke-width="1.4"/><path d="M2.5 6.5 L5.5 9.5 L11 2.5" fill="none" stroke="#1f55ad" stroke-width="1.8"/></svg>Transfer benches</li>
  </ul>
  <ul class="abs services col2">
    <li><svg width="13" height="13" viewBox="0 0 13 13"><rect x="0.7" y="0.7" width="11.6" height="11.6" fill="none" stroke="#1f55ad" stroke-width="1.4"/><path d="M2.5 6.5 L5.5 9.5 L11 2.5" fill="none" stroke="#1f55ad" stroke-width="1.8"/></svg>CPAP/BiPAP</li>
    <li><svg width="13" height="13" viewBox="0 0 13 13"><rect x="0.7" y="0.7" width="11.6" height="11.6" fill="none" stroke="#1f55ad" stroke-width="1.4"/><path d="M2.5 6.5 L5.5 9.5 L11 2.5" fill="none" stroke="#1f55ad" stroke-width="1.8"/></svg>Hospital beds</li>
    <li><svg width="13" height="13" viewBox="0 0 13 13"><rect x="0.7" y="0.7" width="11.6" height="11.6" fill="none" stroke="#1f55ad" stroke-width="1.4"/><path d="M2.5 6.5 L5.5 9.5 L11 2.5" fill="none" stroke="#1f55ad" stroke-width="1.8"/></svg>Walkers/rollators</li>
    <li><svg width="13" height="13" viewBox="0 0 13 13"><rect x="0.7" y="0.7" width="11.6" height="11.6" fill="none" stroke="#1f55ad" stroke-width="1.4"/><path d="M2.5 6.5 L5.5 9.5 L11 2.5" fill="none" stroke="#1f55ad" stroke-width="1.8"/></svg>Crutches/ canes</li>
    <li><svg width="13" height="13" viewBox="0 0 13 13"><rect x="0.7" y="0.7" width="11.6" height="11.6" fill="none" stroke="#1f55ad" stroke-width="1.4"/><path d="M2.5 6.5 L5.5 9.5 L11 2.5" fill="none" stroke="#1f55ad" stroke-width="1.8"/></svg>Shower chairs</li>
    <li><svg width="13" height="13" viewBox="0 0 13 13"><rect x="0.7" y="0.7" width="11.6" height="11.6" fill="none" stroke="#1f55ad" stroke-width="1.4"/><path d="M2.5 6.5 L5.5 9.5 L11 2.5" fill="none" stroke="#1f55ad" stroke-width="1.8"/></svg>Gel Cushion/mattresses</li>
  </ul>

  <p class="abs delivery">We deliver most Durable Medical Equipment<br>free of charge, directly to your home.</p>

  <svg class="abs call-band" width="671" height="51" viewBox="0 0 671 51"><path d="M250 0 H671 V51 H232 Z" fill="#1f55ad"/></svg>
  <div class="abs insurance">
    <svg width="269" height="90" viewBox="0 0 269 90" class="abs"><path d="M0 0 H269 L232 90 H0 Z" fill="#bcd63a"/></svg>
    <p>We accept MOST<br>insurances as well as<br>Medicare and Medicaid.</p>
  </div>
  <div class="abs call condensed">Call: 573-555-0142, 573-555-0178</div>
</section>

<section class="card back">
  <div class="abs back-head"><h2 class="condensed">Full Service Medical Equipment Provider</h2></div>
  <div class="abs van-frame"><div class="van-photo" role="img" aria-label="White company delivery van parked in front of a brick showroom"></div></div>
  <div class="abs locations">LOCATIONS:</div>
  <div class="abs local">LOCALLY OWNED AND OPERATED</div>
  <p class="abs serve">We proudly serve all of Southeast Missouri from our two locations:</p>

  <div class="abs loc-cell" style="left:30px;width:190px"><b>CAPE GIRARDEAU</b><br>1420 N Ridgeview Ste 8<br>PH. 573-555-0142&nbsp;&nbsp; FAX.<br>573-555-0143</div>
  <div class="abs loc-cell" style="left:228px;width:150px">(Across from Corner<br>Care Pharmacy and<br>next door to Maple<br>Donut Shop)</div>
  <div class="abs loc-cell" style="left:388px;width:139px"><b>SIKESTON</b><br>615 N Elm St<br>PH. 573-555-0178<br>FAX.&nbsp; 573-555-0179</div>
  <div class="abs loc-cell" style="left:536px;width:100px">(Between<br>Heritage Trust<br>bank and Fresh<br>Basket)</div>

  <div class="abs gallery">
    <div class="abs product" style="left:32px;width:91px" role="img" aria-label="Folding walker with front wheels"></div>
    <div class="abs product" style="left:132px;width:116px" role="img" aria-label="Home oxygen concentrator"></div>
    <div class="abs product" style="left:256px;width:141px" role="img" aria-label="Adjustable hospital bed frame"></div>
    <div class="abs product" style="left:405px;width:115px" role="img" aria-label="Nebulizer with mask and tubing"></div>
    <div class="abs product" style="left:527px;width:109px" role="img" aria-label="Red rollator with seat"></div>
  </div>

  <div class="abs visit-band"><h3 class="condensed">CALL US TODAY OR STOP BY ONE OF OUR LARGE SHOWROOMS!</h3></div>
  <p class="abs about">ORVAN Medical Equipment employs RN’s and Respiratory Therapists to assist your physician in getting you the appropriate medical equipment for your specific needs. We have 2 conveniently located showrooms to serve all of Southeast Missouri. <b>Contact us today!</b></p>
</section>

</body>
</html>
```